Thank you for shopping with us business card

We would like a thank you card for our rebranded business. We used to be "Brindle Goods" but are now "Marlow Finds. Old thank you card and new logo will be attached for reference. New thank you card does not have to be same design as old thank you card, but please use new logo.
Shopmart URL is now marlowfinds.shopmart.example
Instagram is @Marlow_Finds
Email is marlowfinds@mailbox.example
Thank you!

Contact Information for Business Card

Shopmart site, email, Instagram

```html
<!DOCTYPE html>
<html lang="en">
<head>
<meta charset="utf-8">
<title>Marlow Finds – Thank You Card</title>
<link rel="stylesheet" href="https://fonts.googleapis.com/css2?family=Poppins:wght@400;500;600&family=Yellowtail&display=swap">
<style>
  :root {
    --page: #eceae6;
    --brand-blue: #0c2f8c;
    --band-blue: #092673;
    --lime: #c6f21d;
    --white: #ffffff;
    --shadow: rgba(10, 20, 50, 0.28);
  }
  * { box-sizing: border-box; margin: 0; padding: 0; }
  html, body { width: 1200px; height: 892px; overflow: hidden; }
  body {
    background: var(--page);
    font-family: "Poppins", sans-serif;
    position: relative;
  }
  .card {
    position: absolute;
    width: 540px;
    height: 309px;
    background: var(--brand-blue);
    color: var(--white);
    box-shadow: 0 12px 28px var(--shadow);
    overflow: hidden;
  }

  /* Front */
  .card--front { left: 70px; top: 500px; }
  .front-brand {
    position: absolute;
    left: 0; right: 0; top: 0; bottom: 0;
    display: flex;
    align-items: center;
    justify-content: center;
    gap: 30px;
  }
  .brand-dot {
    width: 70px; height: 70px;
    border-radius: 50%;
    background: var(--white);
  }
  .brand-divider {
    width: 1.5px; height: 100px;
    background: var(--white);
  }
  .front-name {
    font-weight: 500;
    font-size: 40px;
    line-height: 1.05;
    letter-spacing: 1px;
    text-transform: uppercase;
  }

  /* Back */
  .card--thanks { left: 590px; top: 80px; }
  .thanks-brand {
    position: absolute;
    top: 20px; left: 0; right: 0;
    display: flex;
    align-items: center;
    justify-content: center;
    gap: 10px;
  }
  .thanks-brand .brand-dot { width: 24px; height: 24px; }
  .thanks-brand .brand-divider { height: 32px; width: 1px; }
  .thanks-name {
    font-weight: 500;
    font-size: 11px;
    line-height: 1.15;
    letter-spacing: 0.5px;
    text-transform: uppercase;
  }
  .thanks-script {
    position: absolute;
    top: 54px; left: 0; right: 0;
    text-align: center;
    font-family: "Yellowtail", cursive;
    font-size: 84px;
    line-height: 1;
    color: var(--lime);
  }
  .thanks-heading {
    position: absolute;
    top: 148px; left: 0; right: 0;
    text-align: center;
    font-weight: 500;
    font-size: 20px;
    letter-spacing: 1px;
  }
  .thanks-message {
    position: absolute;
    top: 178px; left: 60px; right: 60px;
    text-align: center;
    font-size: 12px;
    line-height: 1.45;
  }
  .contact-band {
    position: absolute;
    left: 0; right: 0; bottom: 0;
    height: 62px;
    background: var(--band-blue);
    display: flex;
    align-items: center;
    justify-content: space-around;
    padding: 0 14px;
  }
  .contact-item {
    display: flex;
    align-items: center;
    gap: 6px;
    font-size: 9.5px;
    color: var(--lime);
  }
  .contact-item svg { width: 14px; height: 14px; flex: none; }
  .social-square {
    width: 12px; height: 12px;
    border: 1.5px solid var(--lime);
    border-radius: 2px;
    flex: none;
  }
</style>
</head>
<body>

  <section class="card card--thanks">
    <div class="thanks-brand">
      <span class="brand-dot"></span>
      <span class="brand-divider"></span>
      <p class="thanks-name">Marlow<br>Finds</p>
    </div>
    <p class="thanks-script">Thank you!</p>
    <h2 class="thanks-heading">FOR YOUR PURCHASE</h2>
    <p class="thanks-message">Your purshace made my day and I hope this package brightens your. Please come back and leave a review</p>
    <footer class="contact-band">
      <span class="contact-item">
        <svg viewBox="0 0 16 16" fill="none" stroke="currentColor" stroke-width="1.2">
          <circle cx="8" cy="8" r="6.5"/>
          <ellipse cx="8" cy="8" rx="3" ry="6.5"/>
          <line x1="1.5" y1="8" x2="14.5" y2="8"/>
          <line x1="2.5" y1="4.8" x2="13.5" y2="4.8"/>
          <line x1="2.5" y1="11.2" x2="13.5" y2="11.2"/>
        </svg>
        marlowfinds.shopmart.example
      </span>
      <span class="contact-item">
        <span class="social-square"></span>
        @Marlow_Finds
      </span>
      <span class="contact-item">
        <svg viewBox="0 0 16 16" fill="none" stroke="currentColor" stroke-width="1.2">
          <rect x="1.5" y="3.5" width="13" height="9"/>
          <polyline points="1.5,3.5 8,9 14.5,3.5"/>
        </svg>
        marlowfinds@mailbox.example
      </span>
    </footer>
  </section>

  <section class="card card--front">
    <div class="front-brand">
      <span class="brand-dot"></span>
      <span class="brand-divider"></span>
      <h1 class="front-name">Marlow<br>Finds</h1>
    </div>
  </section>

</body>
</html>
```